Geschäftspapiere für jungen Rechtsanwalt
Zielgruppe
'Junge' Rechtsanwaltskanzlei, die hauptsächlich im Verkehrsrecht tätig ist. Dabei sowohl für Otto-Normalbürger, als auch für Versicherungen.
Aufgabenstellung
Neben Postanschrift, Telefon, Faxnummer und E-Mail-Adresse sind Angaben zur Bankverbindung und Steuernummer erforderlich.
Bitte keine Klassiker, wie z.B. Paragraphenzeichen, Justizia, etc.

```html
<!DOCTYPE html>
<html lang="de">
<head>
<meta charset="utf-8">
<title>Brandt · Osterkamp · Vellmer – Geschäftsausstattung</title>
<link href="https://fonts.googleapis.com/css2?family=Lora:wght@400;500;600&display=swap" rel="stylesheet">
<style>
  :root{
    --bg:#ebebe9;
    --paper:#ffffff;
    --navy:#4d6d8e;
    --rim:#e3e5ee;
    --teal:#3b97ad;
    --ink:#3d5f82;
  }
  *{box-sizing:border-box;margin:0;padding:0}
  html,body{width:1200px;height:900px;overflow:hidden;background:var(--bg)}
  body{position:relative;font-family:'Lora',Georgia,serif;color:var(--ink)}
  .sheet{position:absolute;background:var(--paper);box-shadow:0 3px 10px rgba(0,0,0,.12);overflow:hidden}
  .sheet .art{position:absolute;inset:0;width:100%;height:100%}
  .fill-navy{fill:var(--navy)}
  .fill-rim{fill:var(--rim)}

  .letterhead{left:50px;top:153px;width:420px;height:594px}
  .envelope-front{left:540px;top:50px;width:500px;height:250px}
  .envelope-back{left:540px;top:330px;width:500px;height:250px}
  .card-front{left:540px;top:620px;width:250px;height:150px}
  .card-back{left:820px;top:620px;width:250px;height:150px}

  .contact-list{position:absolute;list-style:none;display:flex;flex-direction:column}
  .contact-list li{display:flex;align-items:center;white-space:nowrap}
  .icon{flex:none;background:var(--teal);display:inline-flex;align-items:center;justify-content:center}
  .icon svg{width:70%;height:70%}

  .letterhead .contact-list{left:28px;top:52px;gap:10px;font-size:12.5px}
  .letterhead .icon{width:22px;height:22px;margin-right:9px}
  .date-field{position:absolute;left:210px;top:34px;font-size:10px;letter-spacing:.05em;display:flex;align-items:flex-end;gap:8px}
  .date-field .rule{width:110px;border-bottom:1px solid #c9ced8;height:9px}

  .envelope-front .contact-list{gap:8px;font-size:8.5px}
  .envelope-front .icon{width:14px;height:14px;margin-right:6px}
  .envelope-front .col-a{left:200px;top:150px}
  .envelope-front .col-b{left:360px;top:150px}

  .flap{position:absolute;left:0;top:0;width:100%;height:74px;background:var(--navy);border-radius:0 0 26px 26px}

  .card-back .contact-list{left:22px;top:46px;gap:6px;font-size:8.5px}
  .card-back .icon{width:14px;height:14px;margin-right:6px}

  .firm{position:absolute;left:44px;right:12px;top:40px;text-align:center}
  .firm-name{font-size:10.5px;font-weight:500;letter-spacing:.02em;white-space:nowrap;padding-bottom:4px;border-bottom:1px solid var(--ink)}
  .firm-tag{font-size:9px;margin-top:4px;white-space:nowrap}
</style>
</head>
<body>

<svg width="0" height="0" style="position:absolute" aria-hidden="true">
  <defs>
    <symbol id="ico-phone" viewBox="0 0 24 24"><path fill="#fff" d="M6.6 10.8a15 15 0 0 0 6.6 6.6l2.2-2.2a1 1 0 0 1 1-.25 11.4 11.4 0 0 0 3.6.57 1 1 0 0 1 1 1V20a1 1 0 0 1-1 1A17 17 0 0 1 3 4a1 1 0 0 1 1-1h3.5a1 1 0 0 1 1 1c0 1.25.2 2.45.57 3.57a1 1 0 0 1-.25 1z"/></symbol>
    <symbol id="ico-pin" viewBox="0 0 24 24"><path fill="#fff" d="M12 2a7 7 0 0 0-7 7c0 5.2 7 13 7 13s7-7.8 7-13a7 7 0 0 0-7-7zm0 9.5A2.5 2.5 0 1 1 12 6.5a2.5 2.5 0 0 1 0 5z"/></symbol>
    <symbol id="ico-mail" viewBox="0 0 24 24"><path fill="none" stroke="#fff" stroke-width="1.6" d="M3 6h18v12H3zM3 6l9 7 9-7M3 18l7-6M21 18l-7-6"/></symbol>
    <symbol id="ico-fax" viewBox="0 0 24 24"><path fill="#fff" d="M7 3h10v5H7zM4 9h16v8h-3v4H7v-4H4zm5 6v4h6v-4z"/></symbol>
  </defs>
</svg>

<section class="sheet letterhead">
  <svg class="art" viewBox="0 0 420 594" preserveAspectRatio="none" aria-hidden="true">
    <path class="fill-rim" d="M186,0 H420 V188 C388,80 296,30 186,0 Z"/>
    <path class="fill-navy" d="M200,0 H420 V170 C390,70 300,24 200,0 Z"/>
    <path class="fill-rim" d="M0,392 C35,500 140,544 270,544 C310,544 345,566 370,594 H0 Z"/>
    <path class="fill-navy" d="M0,410 C35,505 140,552 260,552 C300,552 330,570 350,594 H0 Z"/>
  </svg>
  <div class="date-field"><span>DATE</span><span class="rule"></span></div>
  <ul class="contact-list">
    <li><span class="icon"><svg><use href="#ico-phone"/></svg></span>+49 (0) 22 1 - 48 26 -300</li>
    <li><span class="icon"><svg><use href="#ico-pin"/></svg></span>Lindenwall 14 D-50321 Cologne</li>
    <li><span class="icon"><svg><use href="#ico-mail"/></svg></span>info@bov-law.de</li>
    <li><span class="icon"><svg><use href="#ico-fax"/></svg></span>+49 (0) 22 1 - 48 26 -370</li>
  </ul>
</section>

<section class="sheet envelope-front">
  <svg class="art" viewBox="0 0 500 250" preserveAspectRatio="none" aria-hidden="true">
    <path class="fill-rim" d="M285,0 H500 V132 C470,56 400,18 285,0 Z"/>
    <path class="fill-navy" d="M300,0 H500 V118 C472,50 402,16 300,0 Z"/>
    <path class="fill-rim" d="M0,128 C30,196 110,236 235,240 L262,250 H0 Z"/>
    <path class="fill-navy" d="M0,142 C30,204 110,242 225,246 L236,250 H0 Z"/>
  </svg>
  <ul class="contact-list col-a">
    <li><span class="icon"><svg><use href="#ico-phone"/></svg></span>+49 (0) 22 1 - 48 26 -300</li>
    <li><span class="icon"><svg><use href="#ico-pin"/></svg></span>Lindenwall 14 D-50321 Cologne</li>
  </ul>
  <ul class="contact-list col-b">
    <li><span class="icon"><svg><use href="#ico-mail"/></svg></span>info@bov-law.de</li>
    <li><span class="icon"><svg><use href="#ico-fax"/></svg></span>+49 (0) 22 1 - 48 26 -370</li>
  </ul>
</section>

<section class="sheet envelope-back">
  <div class="flap"></div>
</section>

<section class="sheet card-front">
  <svg class="art" viewBox="0 0 250 150" preserveAspectRatio="none" aria-hidden="true">
    <path class="fill-rim" d="M0,20 C18,80 70,112 150,112 C180,112 205,118 215,150 H0 Z"/>
    <path class="fill-navy" d="M0,32 C20,90 72,120 150,120 C175,120 195,130 200,150 H0 Z"/>
  </svg>
  <div class="firm">
    <div class="firm-name">BRANDT · OSTERKAMP · VELLMER</div>
    <div class="firm-tag">Rechtsanwälte Partnerschaft</div>
  </div>
</section>

<section class="sheet card-back">
  <svg class="art" viewBox="0 0 250 150" preserveAspectRatio="none" aria-hidden="true">
    <path class="fill-rim" d="M100,0 H250 V110 C232,50 190,14 100,10 Z"/>
    <path class="fill-navy" d="M110,0 H250 V90 C230,36 185,6 110,0 Z"/>
  </svg>
  <ul class="contact-list">
    <li><span class="icon"><svg><use href="#ico-phone"/></svg></span>+49 (0) 22 1 - 48 26 -300</li>
    <li><span class="icon"><svg><use href="#ico-pin"/></svg></span>Lindenwall 14 D-50321 Cologne</li>
    <li><span class="icon"><svg><use href="#ico-mail"/></svg></span>info@bov-law.de</li>
    <li><span class="icon"><svg><use href="#ico-fax"/></svg></span>+49 (0) 22 1 - 48 26 -370</li>
  </ul>
</section>

</body>
</html>
```